Staff Newsletter Template Image

We are looking for two .jpg images that we can put into a Word document and use for our staff newsletter. We will then add content using text boxes.
Attached is the current template which works for the columns and size that we need but we just want a fresh new design.
The Word document shows how we use it.
The name will stay the same - Team upBeat but can be a different look to the current one.

Target Market(s)

Sales team

Colors

Designer to choose colors to be used in the design.

Requirements
Must have
• Colours will be green, grey and white, possibly cream if needed. All from the guidelines.
• I have attached our brand guidelines which shows design elements and fonts for our brand. Also attached is brand guidelines for one of our product lines as we would like to use the same green.
• It needs to be nice to look at and motivational for our team

```html
<!DOCTYPE html>
<html lang="en">
<head>
<meta charset="utf-8">
<title>Team upBeat – Staff Newsletter</title>
<link href="https://fonts.googleapis.com/css2?family=Montserrat:wght@800&display=swap" rel="stylesheet">
<style>
  :root {
    --charcoal: #3a3b3b;
    --green-light: #8cc63f;
    --green-mid: #7db743;
    --paper: #ffffff;
  }
  html, body {
    margin: 0;
    padding: 0;
    overflow: hidden;
    background: var(--paper);
  }
  .newsletter {
    position: relative;
    width: 884px;
    height: 1200px;
    background: var(--paper);
    overflow: hidden;
  }
  .newsletter__shapes {
    position: absolute;
    inset: 0;
    width: 884px;
    height: 1200px;
  }
  .shape--charcoal { fill: var(--charcoal); }
  .shape--green-light { fill: var(--green-light); }
  .shape--green-mid { fill: var(--green-mid); }
  .masthead__name {
    position: absolute;
    left: 52px;
    top: 74px;
    margin: 0;
    white-space: nowrap;
    font-family: "Montserrat", Arial, sans-serif;
    font-weight: 800;
    font-size: 38px;
    line-height: 1;
    letter-spacing: 0.5px;
    color: var(--paper);
  }
</style>
</head>
<body>
  <main class="newsletter">
    <svg class="newsletter__shapes" viewBox="0 0 578 785" preserveAspectRatio="none" aria-hidden="true">
      <polygon class="shape--charcoal" points="0,0 578,0 578,90 95,160 0,110"/>
      <polygon class="shape--green-light" points="0,100 95,148 207,203 0,163"/>
      <polygon class="shape--green-mid" points="95,148 470,95.2 500,112 207,203"/>
      <polygon class="shape--green-light" points="430,100.8 578,80 578,135 500,112"/>
      <polygon class="shape--green-light" points="0,703 135,785 0,785"/>
      <polygon class="shape--charcoal" points="83,752 453,707 578,757 578,785 83,785"/>
    </svg>
    <h1 class="masthead__name">Team upBeat</h1>
  </main>
</body>
</html>
```